DL size flyer for Autism Consultancy website

We need a printed flyer DL size ( 210mmx99mm) for our Autism Consultancy website www.kowharaikids.nz which provides therapy for autistic children.
I want the flyer to look consistent with the website’s design. Please feel free to use the colour scheme, fonts, icons or any images from www.kowharaikids.nz.It should be easy to see “Autism” or “Autistic” word from a distance.
Please use either an oversized logo or make “Do you have a verbal and able autistic child?” more prominent.
Please do not convert the text fields to outlines, i.e. I need to be able to edit any text after.The final design should be either in Adobe Illustrator or Adobe Photoshop format.
The Specs for the flyer are
Document Trim Size99 x 210 mm 1169 x 2480 pixels
Full Bleed Size102 x 213 mm 1205 x 2516 pixels
Our Logo https://1drv.ms/u/s!AoH0rRjDY2GYg6QtU-xjoVlmslKp6gPlease
use this photo for the front side https://filevault.example/u/p8Jd2XcQw5Nv6LtK0rBg3aMf
another one for reverse
https://filevault.example/u/h4Ys7EnRb1Zo9GuP2wCk5jTl
Please use the following content:
Do you have a verbal and able autistic child?
We use child-centred, modern and innovative approaches
Teaching autistic children to bond, laugh and play.
We work with schools
We help autistic children to develop social minds
We offer:
• Specialist assessments
• Consultations for parents & schools
• Social learning programmes
• Social-cognitive therapy
We can create an individual learning path, best suited for your child.
Our programmes and interventions include:
• Bright Lanterns
• Kite Makers
• Pebble Circle
• Harbour Steps
• Puffin Pages
• Wexmoor Speech Ladder
• Tolvar Method
• PLOVIR Method
• Mirrorwood Echo Routine
contact details on both sides:
www.kowharaikids.nz
info@kowharaikids.nz
(09) 57-318-63

```html
<!DOCTYPE html>
<html lang="en">
<head>
<meta charset="utf-8">
<title>Kowharai Kids – DL Flyer</title>
<link rel="stylesheet" href="https://fonts.googleapis.com/css2?family=Roboto:wght@500;700&family=Open+Sans:wght@600;700&family=Roboto+Slab:wght@700&family=Source+Sans+3:wght@400&display=swap">
<style>
:root{
  --backdrop:#7a5030;
  --teal:#55c4c4;
  --teal-light:#8dd8d8;
  --navy:#1d2b55;
  --orange:#f47b20;
  --blue:#3c4fa8;
  --yellow:#fdd22b;
  --paper:#f7f8fa;
  --ink:#111111;
  --phone-teal:#1aa6b7;
}
*{margin:0;padding:0;box-sizing:border-box}
html,body{width:1154px;height:1200px;overflow:hidden;background:var(--backdrop)}
.flyer{position:absolute;top:150px;width:425px;height:900px;background:var(--paper);overflow:hidden}
.flyer--front{left:142px}
.flyer--back{left:614px}
.abs{position:absolute}

/* front */
.hero-band{left:0;top:0;width:425px;height:135px}
.hero-title{left:34px;top:28px;width:380px;font:700 25px/33px "Roboto",sans-serif;color:#fff}
.section-title{font:700 21px/27px "Roboto",sans-serif;color:var(--orange)}
.offer-title{left:34px;top:149px}
.bullets{list-style:none;font:400 14.5px/22.5px "Source Sans 3",sans-serif;color:var(--ink)}
.bullets li{position:relative;padding-left:19px}
.bullets li::before{content:"";position:absolute;left:0;top:7px;width:9px;height:9px;border-radius:50%;background:var(--phone-teal)}
.offer-list{left:34px;top:183px}
.path-band{left:0;top:285px;width:425px;height:72px;background:var(--navy);padding:8px 34px;font:500 21.5px/30px "Roboto",sans-serif;color:#fff}
.programmes-title{left:34px;top:372px;font-family:"Open Sans",sans-serif;font-weight:600;font-size:21px;line-height:28px}
.programme-list{left:34px;top:436px;font-size:14.5px;line-height:19.7px}
.photo{background:linear-gradient(160deg,#e9d6c8,#c89a8a 55%,#6a5a58)}
.photo--tutor{left:263px;top:388px;width:146px;height:189px}
.photo--cars{left:263px;top:585px;width:146px;height:216px;background:linear-gradient(150deg,#d7b48c,#c79b6e 50%,#b65a4a)}
.brand{display:flex;align-items:center;gap:10px;font:700 22px/1 "Roboto",sans-serif;color:var(--navy)}
.brand-dot{width:26px;height:26px;border-radius:50%;background:var(--yellow)}
.brand small{display:block;font:500 13px/1 "Roboto",sans-serif;color:var(--navy);margin-top:6px;letter-spacing:.5px}
.front-brand{left:34px;top:705px}
.front-phone{left:34px;top:779px;font:700 31px/40px "Open Sans",sans-serif;color:var(--phone-teal)}
.front-email{left:34px;top:820px;font:600 16.5px/22px "Open Sans",sans-serif;color:var(--navy);letter-spacing:.3px}
.yellow-bar{left:0;top:848px;width:425px;height:52px;background:var(--yellow);font:700 31px/52px "Open Sans",sans-serif;color:var(--ink);text-align:center}

/* back */
.back-photo{left:0;top:0;width:425px;height:340px;background:linear-gradient(120deg,#b86a48 0%,#e8e3df 35%,#f2efe9 60%,#d7a07a 100%)}
.back-url{left:34px;top:26px;font:700 20px/26px "Open Sans",sans-serif;color:var(--ink)}
.back-waves{left:0;top:250px;width:425px;height:420px}
.question{left:0;top:354px;width:425px;text-align:center;font:700 37px/41px "Open Sans",sans-serif;color:#fff}
.approach{left:0;top:492px;width:425px;text-align:center;font:700 22px/31px "Roboto",sans-serif;color:var(--ink)}
.divider{left:62px;top:562px;width:302px;height:1px;background:#fff}
.bond{left:0;top:574px;width:425px;text-align:center;font:700 22px/28px "Roboto",sans-serif;color:var(--ink)}
.schools{left:0;top:668px;width:425px;text-align:center;font:700 29px/38px "Roboto Slab",serif;color:var(--orange)}
.back-brand{left:110px;top:730px}
.back-email{left:0;top:822px;width:425px;text-align:center;font:600 17px/22px "Open Sans",sans-serif;color:var(--navy);letter-spacing:.3px}
</style>
</head>
<body>

<section class="flyer flyer--front">
  <svg class="abs hero-band" viewBox="0 0 425 135" preserveAspectRatio="none" aria-hidden="true">
    <path d="M0 0H425V118C370 104 320 138 250 124C180 110 120 136 60 122C30 116 12 120 0 124Z" fill="var(--teal-light)"/>
    <path d="M0 0H425V108C360 96 310 126 240 114C170 102 110 124 50 112C25 107 10 110 0 114Z" fill="var(--teal)"/>
  </svg>
  <h1 class="abs hero-title">We help autistic children to develop social minds</h1>

  <h2 class="abs section-title offer-title">We Offer:</h2>
  <ul class="abs bullets offer-list">
    <li>Specialist assessments</li>
    <li>Consultations for parents &amp; schools</li>
    <li>Social learning programmes</li>
    <li>Social-cognitive therapy</li>
  </ul>

  <p class="abs path-band">We can create an individual learning path, best suited for your child.</p>

  <h2 class="abs section-title programmes-title">Our programmes and<br>interventions include:</h2>
  <ul class="abs bullets programme-list">
    <li>Bright Lanterns</li>
    <li>Kite Makers</li>
    <li>Pebble Circle</li>
    <li>Harbour Steps</li>
    <li>Puffin Pages</li>
    <li>Wexmoor Speech Ladder</li>
    <li>Tolvar Method</li>
    <li>PLOVIR Method</li>
    <li>Mirrorwood Echo Routine</li>
  </ul>

  <div class="abs photo photo--tutor" role="img" aria-label="Photo of a therapist and a young girl looking at a drawing together"></div>
  <div class="abs photo photo--cars" role="img" aria-label="Photo of a boy lying on the floor playing with toy cars"></div>

  <div class="abs brand front-brand"><span class="brand-dot"></span><span>Kowharai Kids<small>CONSULTANCY</small></span></div>

  <p class="abs front-phone">(09) 57-318-63</p>
  <p class="abs front-email">info@kowharaikids.nz</p>
  <p class="abs yellow-bar">www.kowharaikids.nz</p>
</section>

<section class="flyer flyer--back">
  <div class="abs back-photo" role="img" aria-label="Photo of a smiling boy holding a teddy bear with a therapist"></div>
  <p class="abs back-url">www.kowharaikids.nz</p>
  <svg class="abs back-waves" viewBox="0 0 425 420" preserveAspectRatio="none" aria-hidden="true">
    <path d="M0 80C70 38 170 20 270 22C350 24 400 30 425 32V420H0Z" fill="var(--orange)"/>
    <path d="M0 92C80 52 180 36 280 38C350 40 400 44 425 45V420H0Z" fill="var(--blue)"/>
    <path d="M0 102C85 64 185 50 290 52C355 54 400 56 425 57V420H0Z" fill="#fff"/>
    <path d="M0 112C50 84 130 70 210 66C300 62 380 66 425 70V420H0Z" fill="var(--teal)"/>
    <path d="M0 382C60 372 110 397 180 384C250 372 300 396 360 386C390 381 410 384 425 387V420H0Z" fill="var(--teal-light)"/>
    <path d="M0 397C70 387 120 412 200 398C270 386 320 410 380 400C400 397 415 399 425 402V420H0Z" fill="var(--paper)"/>
  </svg>
  <h1 class="abs question">Do you have a verbal<br>and able autistic<br>child?</h1>
  <p class="abs approach">We use child-centred, modern<br>and innovative approaches</p>
  <div class="abs divider"></div>
  <p class="abs bond">Teaching autistic children to<br>bond, laugh and play.</p>
  <h2 class="abs schools">We work with schools</h2>
  <div class="abs brand back-brand"><span class="brand-dot"></span><span>Kowharai Kids<small>CONSULTANCY</small></span></div>
  <p class="abs back-email">Email Us: info@kowharaikids.nz</p>
  <p class="abs yellow-bar">Call Us: (09) 57-318-63</p>
</section>

</body>
</html>
```